Security Officer Training Certifications POSTCARD

We need Post Card Design
-Front and Back
-In Compliance with MERLO PRESS for upload!
-For Oversized and Jumbo Size Cards (merlo presses)
Our Company:
www.brandelhollowacademy.org (FOR IDEAS)
We provide Corporate Security Officer/Criminal Justice/Police Tactics Training for Private Companies that have a security department and officers.
We provide:
Handcuffing certifications
Pepper Spray
Compliance Training
Instructor Training
California Guard Card
Our Card to display powerful image for a Security Officer Department
Traits in Pic and Deigns
VALUE
COMPETITIVE EDGE
PROFESSIONAL GROWTH
QUALITY
PROFICIENT/EFFECTIVE SECURITY OFFICERS
TACTICAL OFFICERS
PROFESSIONALISM
EXPERTS
INDUSTRY LEADERS
READINESS
FRONT DESIGN TO BE VERY CATCH AND ATTRACTIVE!
-Please put the images of lawn enforcement, security guards, public safety department in the FRONT
BACK OF THE CARD DESIGN
-Please put our Services/Menu, CREATIVE and CATCHY, in columns and with vivid colors.

```html
<!DOCTYPE html>
<html lang="en">
<head>
<meta charset="utf-8">
<title>Security Officer Training Postcard</title>
<link href="https://fonts.googleapis.com/css2?family=Oswald:wght@300;400;500;600&family=Open+Sans:wght@400;600;700&display=swap" rel="stylesheet">
<style>
  :root {
    --ink: #211f2b;
    --ink-deep: #16151d;
    --silver-light: #f2f2f4;
    --silver-mid: #b9bbc2;
    --silver-dark: #6f727b;
    --white: #ffffff;
    --page: #e6e6e8;
    --muted: #c9cad0;
    --plate: #c3c5cb;
  }
  * { box-sizing: border-box; margin: 0; padding: 0; }
  html, body { width: 1200px; height: 960px; overflow: hidden; }
  body { background: var(--page); position: relative; font-family: "Oswald", sans-serif; }

  .card {
    position: absolute; left: 270px; width: 660px; height: 430px;
    overflow: hidden; box-shadow: 0 6px 18px rgba(0,0,0,.18);
  }
  .card--front { top: 40px; background: var(--ink); }
  .card--back  { top: 500px; background: var(--white); }
  .card svg.art { position: absolute; inset: 0; }

  /* ---------- front ---------- */
  .front-title {
    position: absolute; left: 22px; top: 22px; width: 280px;
    color: var(--white); font-weight: 400; font-size: 25px; line-height: 1.25;
    letter-spacing: .2px; transform: scaleX(.86); transform-origin: left;
  }
  .title-rule {
    position: absolute; left: 18px; top: 96px; width: 250px; height: 5px;
    background: linear-gradient(90deg, var(--silver-light), var(--silver-dark) 80%, transparent);
  }
  .provide-tab {
    position: absolute; left: 16px; top: 118px; width: 160px; height: 28px;
    background: linear-gradient(90deg, var(--silver-light), var(--silver-mid));
    clip-path: polygon(0 0, 100% 0, 92% 100%, 0 100%);
    color: var(--ink); font-size: 15px; padding: 3px 0 0 10px;
  }
  .service-list { position: absolute; left: 24px; top: 160px; list-style: none; }
  .service-list li {
    color: var(--white); font-weight: 300; font-size: 14.5px; line-height: 24px;
    display: flex; align-items: center; gap: 9px;
  }
  .tick { width: 9px; height: 9px; flex: none; }
  .traits {
    position: absolute; left: 22px; top: 292px; width: 300px;
    color: var(--muted); font-weight: 300; font-size: 11.5px; line-height: 17.5px;
  }
  .call-bar {
    position: absolute; left: 0; top: 382px; width: 320px; height: 48px;
    background: linear-gradient(90deg, var(--silver-light), var(--silver-mid) 70%, var(--silver-dark));
    clip-path: polygon(0 0, 100% 0, 92% 100%, 0 100%);
    color: var(--ink-deep); font-size: 22px; font-weight: 500;
    padding: 8px 0 0 20px;
  }
  .call-bar .lead { font-size: 19px; margin-right: 8px; }
  .front-web {
    position: absolute; right: 22px; bottom: 12px;
    font-family: "Open Sans", sans-serif; font-size: 11.5px; color: var(--white); letter-spacing: .3px;
  }

  /* ---------- back ---------- */
  .back-title {
    position: absolute; left: 24px; top: 26px; color: var(--white);
    font-family: "Open Sans", sans-serif; font-weight: 700; font-size: 18px; letter-spacing: .3px;
  }
  .back-rule {
    position: absolute; left: 22px; top: 56px; width: 300px; height: 4px;
    background: linear-gradient(90deg, var(--silver-light), var(--silver-dark) 80%, transparent);
  }
  .program { position: absolute; left: 22px; width: 400px; display: flex; gap: 14px; }
  .program-mark {
    width: 52px; height: 52px; flex: none; border-radius: 50%;
    background: var(--silver-dark);
  }
  .program h3 {
    font-family: "Open Sans", sans-serif; font-weight: 700; font-size: 11px;
    color: var(--white); border-bottom: 1px solid var(--silver-mid); padding-bottom: 2px; margin-bottom: 3px;
  }
  .program p {
    font-family: "Open Sans", sans-serif; font-size: 9px; line-height: 12px; color: var(--muted);
  }
  .back-call {
    position: absolute; left: 0; bottom: 0; width: 250px; height: 40px;
    background: linear-gradient(90deg, var(--silver-light), var(--silver-mid) 70%, var(--silver-dark));
    clip-path: polygon(0 0, 100% 0, 93% 100%, 0 100%);
    font-family: "Open Sans", sans-serif; font-weight: 700; color: var(--ink-deep);
    font-size: 14px; padding: 11px 0 0 18px;
  }
  .back-call .lead { font-size: 11px; margin-right: 6px; }
  .back-web {
    position: absolute; left: 270px; bottom: 14px;
    font-family: "Open Sans", sans-serif; font-size: 10.5px; color: var(--white);
  }
  .back-seal {
    position: absolute; left: 362px; top: 16px; width: 30px; height: 30px;
    border-radius: 50%; background: var(--plate);
  }
</style>
</head>
<body>

<!-- FRONT -->
<section class="card card--front" aria-label="Postcard front">
  <svg class="art" width="660" height="430" viewBox="0 0 660 430">
    <defs>
      <linearGradient id="silver" x1="0" y1="0" x2="1" y2="1">
        <stop offset="0" stop-color="#f4f4f6"/><stop offset=".5" stop-color="#a7a9b0"/><stop offset="1" stop-color="#5f626a"/>
      </linearGradient>
      <linearGradient id="photoTop" x1="0" y1="0" x2="1" y2="1">
        <stop offset="0" stop-color="#c7d3db"/><stop offset=".6" stop-color="#8ea7bb"/><stop offset="1" stop-color="#5a7897"/>
      </linearGradient>
      <linearGradient id="photoMid" x1="0" y1="0" x2="1" y2="1">
        <stop offset="0" stop-color="#3a4150"/><stop offset="1" stop-color="#151922"/>
      </linearGradient>
      <linearGradient id="photoLow" x1="0" y1="0" x2="1" y2="1">
        <stop offset="0" stop-color="#b9c6cf"/><stop offset=".5" stop-color="#5d7aa0"/><stop offset="1" stop-color="#27324a"/>
      </linearGradient>
    </defs>

    <g role="img" aria-label="Photo collage: security officer with radio, homeland security officer seen from behind, officer's duty belt in a glass corridor">
      <polygon points="330,0 660,0 660,120 470,195" fill="url(#photoTop)"/>
      <polygon points="470,195 660,120 660,330 480,215" fill="url(#photoMid)"/>
      <polygon points="480,215 660,330 660,400 350,400" fill="url(#photoLow)"/>
      <polygon points="330,0 470,195 350,400" fill="url(#photoLow)" opacity=".85"/>
    </g>

    <polygon points="0,0 300,0 385,205 320,400 0,400" fill="#211f2b"/>
    <polygon points="226,0 246,0 330,215 300,215" fill="url(#silver)" opacity=".55"/>
    <polygon points="300,0 314,0 400,205 386,205" fill="url(#silver)"/>
    <polygon points="386,205 400,205 336,400 322,400" fill="url(#silver)"/>
    <polygon points="470,195 660,112 660,122 480,205" fill="#211f2b"/>
    <polygon points="480,215 660,322 660,334 474,225" fill="#211f2b"/>
    <rect x="0" y="400" width="660" height="30" fill="#211f2b"/>

    <ellipse role="img" aria-label="Partner badge placeholder" cx="405" cy="205" rx="56" ry="72" fill="#c3c5cb"/>
  </svg>

  <h1 class="front-title">SECURITY OFFICER TRAINING CERTIFICATIONS</h1>
  <div class="title-rule"></div>
  <div class="provide-tab">WE PROVIDE:</div>
  <ul class="service-list">
    <li><svg class="tick" viewBox="0 0 10 10"><rect x=".5" y=".5" width="9" height="9" fill="none" stroke="#fff"/><path d="M2 5l2 2 4-4" fill="none" stroke="#fff" stroke-width="1.2"/></svg>HANDCUFFING CERTIFICATIONS</li>
    <li><svg class="tick" viewBox="0 0 10 10"><rect x=".5" y=".5" width="9" height="9" fill="none" stroke="#fff"/><path d="M2 5l2 2 4-4" fill="none" stroke="#fff" stroke-width="1.2"/></svg>PEPPER SPRAY</li>
    <li><svg class="tick" viewBox="0 0 10 10"><rect x=".5" y=".5" width="9" height="9" fill="none" stroke="#fff"/><path d="M2 5l2 2 4-4" fill="none" stroke="#fff" stroke-width="1.2"/></svg>COMPLIANCE TRAINING</li>
    <li><svg class="tick" viewBox="0 0 10 10"><rect x=".5" y=".5" width="9" height="9" fill="none" stroke="#fff"/><path d="M2 5l2 2 4-4" fill="none" stroke="#fff" stroke-width="1.2"/></svg>INSTRUCTOR TRAINING</li>
    <li><svg class="tick" viewBox="0 0 10 10"><rect x=".5" y=".5" width="9" height="9" fill="none" stroke="#fff"/><path d="M2 5l2 2 4-4" fill="none" stroke="#fff" stroke-width="1.2"/></svg>CALIFORNIA GUARD CARD</li>
  </ul>
  <p class="traits">VALUE • COMPETITIVE EDGE • PROFESSIONAL GROWTH<br>QUALITY • PROFICIENT/EFFECTIVE SECURITY OFFICERS<br>TACTICAL OFFICERS • PROFESSIONALISM • EXPERTS<br>INDUSTRY LEADERS • READINESS</p>
  <div class="call-bar"><span class="lead">CALL NOW!</span>(555) 014-2290</div>
  <p class="front-web">www.brandelhollowacademy.org</p>
</section>

<!-- BACK -->
<section class="card card--back" aria-label="Postcard back">
  <svg class="art" width="660" height="430" viewBox="0 0 660 430">
    <polygon points="0,0 440,0 470,430 0,430" fill="#211f2b"/>
  </svg>
  <div class="back-seal" role="img" aria-label="Partner badge placeholder"></div>

  <h2 class="back-title">SECURITY OFFICER ACADEMY</h2>
  <div class="back-rule"></div>

  <article class="program" style="top:78px">
    <div class="program-mark" role="img" aria-label="Program emblem placeholder"></div>
    <div>
      <h3>CERTIFIED PROTECTION OFFICER (CPO)</h3>
      <p>This basic program allows you entry level positions in security!<br>• California Guard Card License!<br>• Powers to Arrest</p>
    </div>
  </article>

  <article class="program" style="top:160px">
    <div class="program-mark" role="img" aria-label="Program emblem placeholder"></div>
    <div>
      <h3>CERTIFIED FIREARMS OFFICER (CFO)</h3>
      <p>Program is designed for Advanced employment in the security field.<br>• California Guard Card license! • Exposed Firearms License!<br>• Pepper Spray Permit! • Workplace Violence!<br>• Handling Difficult People!</p>
    </div>
  </article>

  <article class="program" style="top:262px">
    <div class="program-mark" role="img" aria-label="Program emblem placeholder"></div>
    <div>
      <h3>SECURITY OFFICER ACADEMY (SOA)</h3>
      <p>Program is designed for beginner and advanced security officers.<br>• Certified Protection Officer<br>• Certified Firearms Officer<br>• Accredited First Aid/CPR AED</p>
    </div>
  </article>

  <div class="back-call"><span class="lead">CALL NOW!</span>(555) 014-2290</div>
  <p class="back-web">www.brandelhollowacademy.org</p>
</section>

</body>
</html>
```